Coach/consultant in conflict and challenge needs an enticing flyer

I need a double sided DL flyer design that will describe my work in helping people meet conflict and emotional challenge so they can learn and grow from these difficulties. I want to give a flavour of my style through fresh colours, repeated images used differently (the spiral), and a sense of positivity around conflict and difficulty. I want to attract people who are keen to do things differently and want to engage with creative processes rather than getting stuck in familiar patterns. My work is creative and often includes use of story, images and fables, so I want to convey that as well. I also place the work in a spiritual context, but grounded in practicality so I don't want it to seem New Age or flakey. I want something that seems innovative, professional and intriguing. I've included a sample of something I mocked up in word and also a copy of a flyer for Marla Quennet's Ember Gathering that inspired me to get a DL flyer. I want the design to communicate trust and transformation and engaging with fresh ways of doing things by moving past old habits

Target Market(s)

Mid 30s plus women and men who want to change their approach to conflict and emotional difficulties and are willing to take the creative and challenging journey to do that

Industry/Entity Type

Learn

Colors
acd136
00a990

Requirements
Must have
• a shift in the use of the spiral image,
• use of image of me (Norah)
• bright fresh colours olours that represent growth and transformation--I've suggested lime green as it suggests a sense of growth
• easy to read text
Nice to have
• Interesting non-traditional fonts perhaps text in a contemporary sans serif and another brush script font (like the Ember Gathering example)
• bleed to the edge and run off the page images or text
Should not have
• anything that represents too much tradition or stuckness

```html
<!DOCTYPE html>
<html lang="en">
<head>
<meta charset="utf-8">
<title>Norah Vantreece – DL Flyer</title>
<link href="https://fonts.googleapis.com/css2?family=Cabin:wght@400;500;600&family=Arimo&family=Yesteryear&display=swap" rel="stylesheet">
<style>
  :root {
    --lime: #acd136;
    --lime-light: #c3df5e;
    --lime-pale: #d4e98a;
    --teal: #00a990;
    --white: #ffffff;
    --page: #ecebe8;
    --photo-warm: #d9653a;
    --photo-light: #efe9e4;
  }
  * { margin: 0; padding: 0; box-sizing: border-box; }
  html, body { width: 1200px; height: 1150px; overflow: hidden; background: var(--page); }
  body { position: relative; font-family: "Cabin", sans-serif; color: var(--white); }

  .flyer {
    position: absolute; left: 100px; width: 1000px; height: 476px; overflow: hidden;
    background: radial-gradient(ellipse at 70% 30%, var(--lime-light) 0%, var(--lime) 70%);
    box-shadow: 0 4px 12px rgba(0,0,0,.18);
  }
  .flyer--front { top: 80px; }
  .flyer--back { top: 614px; }

  /* Front */
  .brand { position: absolute; display: flex; align-items: center; }
  .brand__dot { border-radius: 50%; background: var(--teal); flex: none; }
  .front-brand { left: 56px; top: 52px; gap: 34px; }
  .front-brand .brand__dot { width: 150px; height: 150px; }
  .front-brand .brand__name { font-size: 80px; font-weight: 500; color: var(--white); line-height: 1; }
  .hashtags {
    position: absolute; left: 280px; top: 156px; font-size: 33px; font-weight: 500; color: var(--teal);
    word-spacing: 4px;
  }
  .hashtags span { margin-right: 12px; }
  .lead { position: absolute; left: 48px; width: 910px; font-size: 21px; line-height: 28px; }
  .lead--one { top: 254px; }
  .lead--two { top: 359px; }

  /* Back */
  .back-brand { left: 30px; top: 28px; gap: 10px; }
  .back-brand .brand__dot { width: 40px; height: 40px; }
  .back-brand .brand__name { font-size: 28px; font-weight: 500; color: var(--teal); }
  .about { position: absolute; left: 31px; width: 565px; font-size: 16px; line-height: 18.3px; }
  .about--one { top: 84px; }
  .about--two { top: 194px; }
  .services {
    position: absolute; left: 32px; top: 259px; display: grid; grid-template-columns: 155px 120px;
    font-family: "Yesteryear", cursive; font-size: 20px; line-height: 24px; list-style: none;
  }
  .services li::before { content: "• "; }
  .credentials { position: absolute; left: 31px; top: 338px; font-family: "Arimo", sans-serif; font-size: 15px; line-height: 21px; }
  .credentials__name { font-family: "Cabin", sans-serif; font-size: 20px; font-weight: 500; color: var(--teal); }
  .contacts {
    position: absolute; left: 31px; top: 402px; display: grid; grid-template-columns: 236px 240px;
    row-gap: 5px; font-family: "Arimo", sans-serif; font-size: 15px; list-style: none;
  }
  .contacts li { display: flex; align-items: center; gap: 7px; }
  .contacts svg { width: 15px; height: 15px; flex: none; }
  .portrait-frame { position: absolute; left: 0; top: 0; width: 1000px; height: 476px; pointer-events: none; }
</style>
</head>
<body>

<section class="flyer flyer--front">
  <div class="brand front-brand">
    <span class="brand__dot"></span>
    <span class="brand__name">Norah Vantreece</span>
  </div>
  <p class="hashtags"><span># courage</span><span># listening</span><span># creativity</span></p>
  <p class="lead lead--one">Challenge, change and conflict are a natural part of life. When we greet them with courage, and listen to what they tell us, we grow in wisdom, resilience and creativity.</p>
  <p class="lead lead--two">Norah Vantreece is a coach, educator and mediator. She works with people who want to harvest the fruits of challenge and conflict so they live life differently.</p>
</section>

<section class="flyer flyer--back">
  <svg class="portrait-frame" viewBox="0 0 1000 476">
    <defs>
      <linearGradient id="portraitTone" x1="0" y1="0" x2="0" y2="1">
        <stop offset="0" stop-color="var(--photo-light)"/>
        <stop offset="0.55" stop-color="#c9b8a8"/>
        <stop offset="1" stop-color="var(--photo-warm)"/>
      </linearGradient>
    </defs>
    <path d="M700 0 L722 0 Q590 240 690 476 L668 476 Q575 240 700 0 Z" fill="var(--lime-pale)"/>
    <path d="M718 0 L742 0 Q612 240 708 476 L684 476 Q592 240 718 0 Z" fill="var(--teal)"/>
    <path d="M740 0 L1000 0 L1000 476 L706 476 Q610 240 740 0 Z" fill="url(#portraitTone)" role="img" aria-label="Portrait photograph of Norah"/>
  </svg>

  <div class="brand back-brand">
    <span class="brand__dot"></span>
    <span class="brand__name">Norah Vantreece</span>
  </div>
  <p class="about about--one">Consult with Norah to address challenges in your life, relationship, group or organisation. Through listening, conversation and creative processes, you will discover what your challenge is asking of you. Norah Vantreece is a skilled facilitator who works to shift people’s responses from reactivity to creativity.</p>
  <p class="about about--two">With many years’ experience in coaching and mentorship, mediation and narrative processes, Norah supports you to uncover unique responses to difficult situations.</p>
  <ul class="services">
    <li>Consultations</li><li>Speaking</li>
    <li>Workshops</li><li>Articles</li>
  </ul>
  <div class="credentials">
    <p><span class="credentials__name">Norah Vantreece</span> - ABN 41 620 318 75</p>
    <p>PhD, MCR, BAppSci, DipHum, AssDipEd</p>
  </div>
  <ul class="contacts">
    <li><svg viewBox="0 0 16 16"><circle cx="8" cy="8" r="7" fill="none" stroke="var(--teal)" stroke-width="1.5"/><path d="M5.5 4.5 L7 6 L6.2 7 Q7.5 9 9 9.8 L10 9 L11.5 10.5 L10.5 11.5 Q7 11 4.5 5.5 Z" fill="var(--teal)"/></svg>0400 555 012 (m)</li>
    <li><svg viewBox="0 0 16 16"><circle cx="8" cy="8" r="7" fill="var(--teal)"/><rect x="4" y="5.5" width="8" height="5" fill="none" stroke="var(--white)" stroke-width="1"/><path d="M4 5.5 L8 8.5 L12 5.5" fill="none" stroke="var(--white)" stroke-width="1"/></svg>norah@norahvantreece.com</li>
    <li><svg viewBox="0 0 16 16"><circle cx="8" cy="8" r="7" fill="none" stroke="var(--teal)" stroke-width="1.5"/><path d="M5.5 4.5 L7 6 L6.2 7 Q7.5 9 9 9.8 L10 9 L11.5 10.5 L10.5 11.5 Q7 11 4.5 5.5 Z" fill="var(--teal)"/></svg>+61 3 5550 1847 (h)</li>
    <li><svg viewBox="0 0 16 16"><circle cx="8" cy="8" r="7" fill="var(--teal)"/><circle cx="8" cy="8" r="4" fill="none" stroke="var(--white)" stroke-width="1"/><path d="M4 8 H12 M8 4 Q5.5 8 8 12 M8 4 Q10.5 8 8 12" fill="none" stroke="var(--white)" stroke-width="0.8"/></svg>norahvantreece.com</li>
  </ul>
</section>

</body>
</html>
```